Financial Advisor needs waiting room sign

I am a financial advisor that works with a number of accountants to develop prospects. I am looking for a 18"x24" sign to hang in their office waiting rooms to help develop prospect interest in my services. My original idea was to list all of our services in a jumbled way on the sign and on the bottom have something like "Confused? We have the answers?" "Questions - We have answers" Our logo on the bottom. While I think this is still a good idea when I try to design it - it does not work. I am open to other ideas. Here is a list of our services (list in no particular order) and I will attach our logo. List: Plovance, Plovance Supplement, Plovance Advantage, Truvely, Part A, Part B, Part D, Social Security, Turning 65, Annuities, Fixed Index Annuities, Rollovers, 401k, 403b, Investments, Stock Market, Mutual Funds, Term Insurance, Life Insurance, Final Expense, Long Term Care, Mortgage Protection, 403B / 457 Not for Profit Set Up, 403B / TSA Plans, Annuities, Asset Protection, Charitable Giving, College Funding, Estate Planning, Fixed Indexed Annuities, Guaranteed Income, IRA & 401(K) Assets and Planning, IRA, 401(K), 403(B) Rollovers, Lifetime Income Planning, Retirement Income Planning, Safe Money Options, Social Security, Tactical Asset Allocation

```html
<!DOCTYPE html>
<html lang="en">
<head>
<meta charset="utf-8">
<title>Halvery Capital – Waiting Room Sign</title>
<link rel="stylesheet" href="https://fonts.googleapis.com/css2?family=Russo+One&family=Saira+Extra+Condensed:wght@700&display=swap">
<style>
  :root {
    --green: #477a0f;
    --green-dark: #3a6509;
    --paper: #ffffff;
    --backdrop: #f1f1ef;
  }
  * { box-sizing: border-box; margin: 0; padding: 0; }
  html, body {
    width: 1200px; height: 1000px; overflow: hidden;
    background: var(--backdrop);
  }
  .canvas { position: relative; width: 1200px; height: 1000px; }
  .poster {
    position: absolute; left: 250px; top: 20px;
    width: 700px; height: 960px;
    background: var(--paper);
    box-shadow: 0 4px 18px rgba(0,0,0,.15);
    overflow: hidden;
  }
  .outer-band {
    position: absolute; inset: 10px;
    border: 14px solid var(--green);
  }
  .headline-panel {
    position: absolute; left: 40px; right: 40px; top: 38px; height: 425px;
    border: 20px solid var(--green); border-bottom: none;
  }
  .brand {
    position: absolute; top: 118px; left: 0; right: 0;
    display: flex; justify-content: center; align-items: center; gap: 12px;
  }
  .brand-mark {
    width: 40px; height: 40px; border-radius: 50%;
    background: var(--green);
  }
  .brand-text { display: flex; flex-direction: column; }
  .brand-name {
    font-family: "Russo One", sans-serif; font-size: 22px;
    color: var(--green); letter-spacing: 1px; line-height: 1;
  }
  .brand-tagline {
    font-family: "Russo One", sans-serif; font-size: 8.5px;
    color: var(--green); letter-spacing: 2.2px; margin-top: 4px;
  }
  .question {
    position: absolute; top: 250px; left: 0; right: 0; text-align: center;
    font-family: "Russo One", sans-serif; font-size: 76px;
    color: var(--green); letter-spacing: 2px; line-height: 1;
  }
  .services {
    position: absolute; left: 58px; right: 56px; top: 432px; height: 500px;
    overflow: hidden;
    font-family: "Saira Extra Condensed", sans-serif; font-weight: 700;
    font-size: 17.5px; line-height: 16.7px; letter-spacing: .6px;
    text-transform: uppercase; color: var(--green);
    text-align: justify;
  }
  .answer {
    position: absolute; left: 0; right: 0; text-align: center;
    font-family: "Russo One", sans-serif; color: var(--paper);
    line-height: 1; letter-spacing: 1px;
    text-shadow:
      -3px -3px 0 var(--green-dark), 3px -3px 0 var(--green-dark),
      -3px 3px 0 var(--green-dark), 3px 3px 0 var(--green-dark),
      0 -3px 0 var(--green-dark), 0 3px 0 var(--green-dark),
      -3px 0 0 var(--green-dark), 3px 0 0 var(--green-dark),
      6px 6px 0 var(--green-dark);
  }
  .answer-lead { top: 604px; font-size: 60px; }
  .answer-main { top: 668px; font-size: 88px; }
</style>
</head>
<body>
<div class="canvas">
  <div class="poster">
    <div class="outer-band"></div>
    <div class="headline-panel"></div>

    <div class="brand">
      <div class="brand-mark"></div>
      <div class="brand-text">
        <span class="brand-name">HALVERY CAPITAL</span>
        <span class="brand-tagline">INSURANCE AND FINANCIAL SERVICES</span>
      </div>
    </div>

    <h1 class="question">CONFUSED?</h1>

    <p class="services">
      Plovance, Plovance Supplement, Plovance Advantage, Truvely, Part A, Part B, Part D, Social Security, Turning 65, Annuities, Fixed Index Annuities, Rollovers, 401k, 403b, Investments, Stock Market, Mutual Funds, Term Insurance, Life Insurance, Final Expense, Long Term Care, Mortgage Protection, 403B / 457 Not for Profit Set Up, 403B / TSA Plans, Annuities, Asset Protection, Charitable Giving, College Funding, Estate Planning, Fixed Indexed Annuities, Guaranteed Income, IRA &amp; 401(K) Assets and Planning, IRA, 401(K), 403(B) Rolovers, Lifetime Income Planning, Retirement Income Planning, Safe Money Options, Social Security, Tactical Asset Allocation, Plovance, Plovance Supplement, Plovance Advantage, Truvely, Part A, Part B, Part D, Social Security, Turning 65, Annuities, Fixed Index Annuities, Rollovers, 401k, 403b, Investments, Stock Market, Mutual Funds, Term Insurance, Life Insurance, Final Expense, Long Term Care, Mortgage Protection, 403B / 457 Not for Profit Set Up, 403B / TSA Plans, Annuities, Asset Protection, Charitable Giving, College Funding, Estate Planning, Fixed Indexed Annuities, Guaranteed Income, IRA &amp; 401(K) Assets and Planning, IRA, 401(K), 403(B) Rolovers, Lifetime Income Planning, Retirement Income Planning, Safe Money Options, Social Security, Tactical Asset Allocation, Plovance Supplement, Plovance Advantage, Truvely, Part A, Part B, Part D, Social Security, Turning 65, Annuities, Fixed Index Annuities, Rollovers, 401k, 403b, Investments, Stock Market, Mutual Funds, Term Insurance, Life Insurance, Final Expense, Long Term Care, Mortgage Protection, 403B / 457 Not for Profit Set Up, 403B / TSA Plans, Annuities, Asset Protection, Charitable Giving, College Funding, Estate Planning, Fixed Indexed Annuities, Guaranteed Income, IRA &amp; 401(K) Assets and Planning, IRA, 401(K), 403(B) Rolovers, Lifetime Income Planning, Retirement Income Planning, Safe Money Options, Social Security, Tactical Asset Allocation, Plovance Supplement, Plovance Advantage, Truvely, Part A, Part B, Part D, Social Security, Turning 65, Annuities, Fixed Index Annuities, Rollovers, 401k, 403b, Investments, Stock Market, Mutual Funds, Term Insurance, Life Insurance, Final Expense, Long Term Care, Mortgage Protection
    </p>

    <p class="answer answer-lead">WE HAVE THE</p>
    <p class="answer answer-main">ANSWERS</p>
  </div>
</div>
</body>
</html>
```